Logo Design and Business Card Musician

I need a design for a Business Card and a logo for a professional of music industry. His name is Tomas Velarde: composer, arranger and music producer. You can find him in: [login to view URL], although we are now working in some many changes regarding the site environment. The logo can be with the initials T V, T Ve or any other external suggestion. I request (my idea is, but I am so open), three basic colors: black and white (in any combination) and a different colour. Business card will be two faces: the backside with the link to the web and the logo. Tomas Velarde: composer with experience working with artists, tv, theatre… Some adjectives of his personality: direct, energetic, resolute, fresh, his music is a reflect of his personality. No interest in "obvious" symbols like treble clef, a piano… Thank you very much.

Necesito un diseño de una Business Card y el Logo para un profesional del mundo de la música. El nombre es Tomas Velarde: compositor, arreglista y productor musical. Puedes encontrarlo en [login to view URL], aunque estamos en fase de cambio del entorno de la web. Puede tratarse de un logo con las iniciales T V, T Ve o cualquier sugerencia externa. Solicito, en principio, tres colores básicos: negro y blanco (en cualquier combinación) y un color. La Business card será a dos caras: en la trasera irá solo la web y el logo. Tomas Velarde: compositor con experiencia en artistas, televisión, teatro… directo, contundente, enérgico, fresco, su música es reflejo de su personalidad. No estoy muy interesada en símbolos "obvios" como clave de sol, teclas del piano… Muchas gracias.

```html
<!DOCTYPE html>
<html lang="en">
<head>
<meta charset="utf-8">
<title>Tomas Velarde — Business Card</title>
<link rel="stylesheet" href="https://fonts.googleapis.com/css2?family=Cinzel:wght@500&family=Lato:wght@400;700&display=swap">
<style>
  :root {
    --stage: #e8e5e1;
    --paper: #ffffff;
    --ink: #111111;
    --accent: #ee5a12;
    --rule: #1a1a1a;
    --faint: #d9d9d9;
    --night: #050505;
    --night-art: #141414;
    --muted-ink: #333333;
  }
  * { box-sizing: border-box; margin: 0; padding: 0; }
  html, body { width: 1200px; height: 873px; overflow: hidden; }
  body { background: var(--stage); position: relative; font-family: "Lato", sans-serif; }

  .card {
    position: absolute; left: 290px; width: 620px; height: 354px;
    overflow: hidden; box-shadow: 0 6px 18px rgba(0,0,0,.18);
  }
  .card--front { top: 45px; background: var(--paper); }
  .card--back { top: 440px; background: var(--night); }

  /* front */
  .front-art {
    position: absolute; left: 300px; top: 0; width: 320px; height: 354px;
    background: radial-gradient(ellipse at 65% 55%, var(--faint) 0%, rgba(217,217,217,.35) 45%, rgba(255,255,255,0) 75%);
  }
  .front-art--left {
    left: 0; width: 320px;
    background: linear-gradient(90deg, rgba(217,217,217,.45), rgba(255,255,255,0));
  }
  .front-rule { position: absolute; left: 0; right: 0; height: 1px; background: var(--rule); }
  .front-rule--top { top: 24px; }
  .front-rule--bottom { bottom: 30px; }

  .identity-panel {
    position: absolute; left: 0; top: 0; width: 335px; height: 354px;
    background: rgba(255,255,255,.72);
    box-shadow: 4px 0 8px rgba(0,0,0,.18);
  }
  .monogram {
    position: absolute; left: 0; width: 100%; text-align: center;
    font-family: "Lato", sans-serif; font-weight: 700; color: var(--accent);
  }
  .identity-panel .monogram { top: 58px; font-size: 84px; line-height: 1; }
  .name {
    position: absolute; left: 0; width: 100%; text-align: center;
    font-family: "Cinzel", serif; font-weight: 500; color: var(--accent);
    letter-spacing: .06em;
  }
  .identity-panel .name { top: 168px; font-size: 18px; }
  .roles {
    position: absolute; left: 0; width: 100%; text-align: center;
    font-family: "Lato", sans-serif;
  }
  .identity-panel .roles { top: 198px; font-size: 8.5px; font-weight: 700; color: var(--ink); letter-spacing: .03em; }

  .contact-list { position: absolute; left: 343px; top: 86px; list-style: none; }
  .contact-item { display: flex; align-items: center; height: 26px; margin-bottom: 4px; }
  .contact-tab {
    width: 40px; height: 18px; background: var(--ink);
    display: flex; align-items: center; justify-content: flex-end; padding-right: 2px;
  }
  .contact-icon { width: 16px; height: 16px; }
  .contact-text { margin-left: 8px; font-size: 11px; color: var(--muted-ink); line-height: 1.15; }

  /* back */
  .back-art {
    position: absolute; inset: 0;
    background:
      radial-gradient(ellipse at 85% 40%, var(--night-art) 0%, rgba(20,20,20,0) 45%),
      radial-gradient(ellipse at 12% 45%, var(--night-art) 0%, rgba(20,20,20,0) 40%);
  }
  .card--back .monogram { top: 60px; font-size: 120px; line-height: 1; }
  .card--back .name { top: 212px; font-size: 21px; }
  .card--back .roles { top: 262px; font-size: 20px; font-weight: 400; color: var(--paper); letter-spacing: .06em; }
</style>
</head>
<body>

<section class="card card--front" aria-label="Business card front">
  <div class="front-art front-art--left" role="img" aria-label="Faint grey music staff, notes and level meter backdrop"></div>
  <div class="front-art" role="img" aria-label="Faint grey microphone and vinyl record backdrop"></div>
  <div class="front-rule front-rule--top"></div>
  <div class="front-rule front-rule--bottom"></div>

  <div class="identity-panel">
    <div class="monogram">T V</div>
    <div class="name">Tomas Velarde</div>
    <div class="roles">Composer • Arranger • Songwriter • Music Producer</div>
  </div>

  <ul class="contact-list">
    <li class="contact-item">
      <span class="contact-tab">
        <svg class="contact-icon" viewBox="0 0 16 16" aria-hidden="true"><circle cx="8" cy="8" r="7" fill="#fff" stroke="#111" stroke-width="1"/><path d="M5.3 4.5l1.4 1.6-.8 1a5 5 0 0 0 2.9 2.9l1-.8 1.6 1.4-.9 1.1C8 11.5 4.6 8.1 4.2 5.4z" fill="#111"/></svg>
      </span>
      <span class="contact-text">000 . 555 . 0147</span>
    </li>
    <li class="contact-item">
      <span class="contact-tab">
        <svg class="contact-icon" viewBox="0 0 16 16" aria-hidden="true"><circle cx="8" cy="8" r="7" fill="#fff" stroke="#111" stroke-width="1"/><rect x="4.2" y="5.3" width="7.6" height="5.4" fill="none" stroke="#111" stroke-width="1"/><path d="M4.2 5.3L8 8.4l3.8-3.1" fill="none" stroke="#111" stroke-width="1"/></svg>
      </span>
      <span class="contact-text">tomasvelardemusic@mailbox.com</span>
    </li>
    <li class="contact-item">
      <span class="contact-tab">
        <svg class="contact-icon" viewBox="0 0 16 16" aria-hidden="true"><circle cx="8" cy="8" r="7" fill="#fff" stroke="#111" stroke-width="1"/><circle cx="8" cy="8" r="4" fill="none" stroke="#111" stroke-width="1"/><ellipse cx="8" cy="8" rx="1.8" ry="4" fill="none" stroke="#111" stroke-width=".8"/><path d="M4 8h8" stroke="#111" stroke-width=".8"/></svg>
      </span>
      <span class="contact-text">www.tomasvelardemusic.com</span>
    </li>
    <li class="contact-item">
      <span class="contact-tab">
        <svg class="contact-icon" viewBox="0 0 16 16" aria-hidden="true"><circle cx="8" cy="8" r="7" fill="#fff" stroke="#111" stroke-width="1"/><path d="M4 8.2L8 4.6l4 3.6h-1.2v3.4H5.2V8.2z" fill="#111"/></svg>
      </span>
      <span class="contact-text">27 Linden Street<br>Harbor City, NY 100200</span>
    </li>
  </ul>
</section>

<section class="card card--back" aria-label="Business card back">
  <div class="back-art" role="img" aria-label="Dark grey music staff, microphone and vinyl record backdrop"></div>
  <div class="monogram">T V</div>
  <div class="name">Tomas Velarde</div>
  <div class="roles">Composer • Arranger • Songwriter • Music Producer</div>
</section>

</body>
</html>
```